Harbor Vantage Web Design Project

We need a website design for a start up company called "Harbor Vantage". We provide business consultancy services as well as technology-related services (IT). The design should communicate simplicity and elegance. The domain name of the site will be harborvantage-example.com. The logo of the company is https://files.example-share.net/u/7418205/4630_2116587_67315_image.jpg

Target Market(s)

SMB, Corporates, Semi-governments, Governments.

Industry/Entity Type

Business

Requirements
Must have
• - The background of the pages should be white or soft grey, but we are open for suggestions.
- The pages should have nice menu animations.
- The pages should be "portal-style", with multiple placeholders for different sections and multiple tabs.
Nice to have
• The page should auto-fit the screen and scroll vertically as much as needed.
Should not have
• - Flash Animations.
- Generic Photos.

```html
<!DOCTYPE html>
<html lang="en">
<head>
<meta charset="utf-8">
<title>Harbor Vantage</title>
<link href="https://fonts.googleapis.com/css2?family=Oswald:wght@300;400&family=Open+Sans:wght@400;600;700&display=swap" rel="stylesheet">
<style>
:root{
  --red:#d22a2a;
  --dark:#3a3a3a;
  --darker:#2d2d2d;
  --ink:#333;
  --muted:#777;
  --line:#e2e2e2;
  --band:#ebebeb;
  --white:#fff;
}
*{box-sizing:border-box;margin:0;padding:0}
html,body{width:1200px;height:2842px;overflow:hidden;background:var(--white);font-family:"Open Sans",Arial,sans-serif;color:var(--ink)}
.page{position:relative;width:1200px;height:2842px}
.abs{position:absolute}
.h-font{font-family:"Oswald","Arial Narrow",sans-serif}
.ph{position:absolute}
/* header */
.header{position:absolute;left:0;top:0;width:1200px;height:148px;background:linear-gradient(#fff,#f4f4f4)}
.logo{position:absolute;left:40px;top:40px;display:flex;align-items:center;gap:14px}
.logo .mark{width:44px;height:44px;border-radius:50%;background:var(--red)}
.logo .name{font-family:"Open Sans",sans-serif;font-weight:700;font-size:34px;color:var(--red)}
.contact-top{position:absolute;right:40px;top:30px;font-size:14px;color:#666;display:flex;gap:36px}
.search{position:absolute;right:40px;top:78px;width:300px;height:36px;border:1px solid #ccc;background:#fff;font-size:13px;color:#aaa;padding:8px 12px}
.search svg{position:absolute;right:10px;top:10px}
/* nav */
.nav{position:absolute;left:0;top:148px;width:1200px;height:52px;background:var(--dark);display:flex;align-items:center}
.nav .home{width:52px;height:52px;background:var(--red);display:flex;align-items:center;justify-content:center}
.nav a{font-family:"Oswald",sans-serif;color:#eee;font-size:17px;text-decoration:none;padding:0 34px;border-right:1px solid #555;line-height:52px;letter-spacing:.5px}
/* hero */
.hero{position:absolute;left:0;top:200px;width:1200px;height:552px;background:linear-gradient(100deg,#eef1f3 0%,#dfe6ea 45%,#9fb6c4 75%,#5d7688 100%)}
.hero h1{position:absolute;left:62px;top:70px;font-family:"Oswald",sans-serif;font-weight:400;font-size:62px;color:#333;letter-spacing:1px}
.hero h1 span{color:var(--red)}
.hero p{position:absolute;left:62px;top:190px;width:360px;font-size:20px;line-height:32px;color:#444}
.btn{position:absolute;background:#e4e4e4;border-left:5px solid var(--red);color:#444;font-size:18px;display:flex;align-items:center;gap:14px;padding:0 20px}
.hero .btn{left:62px;top:300px;height:50px}
/* feature strip */
.strip{position:absolute;left:0;top:752px;width:1200px;height:116px;background:var(--dark);display:flex}
.strip .item{width:300px;height:116px;display:flex;align-items:center;gap:16px;padding:0 26px}
.strip .item.on{background:#555}
.strip .pic{width:66px;height:66px;flex:none;border:3px solid #fff}
.strip h4{font-weight:600;color:#fff;font-size:16px}
.strip p{color:#aaa;font-size:13px;line-height:18px;margin-top:4px}
/* columns */
.col{position:absolute;top:895px;width:356px}
.col-title{display:flex;align-items:center;gap:12px;font-family:"Oswald",sans-serif;font-size:30px;color:#333;border-bottom:1px solid var(--line);padding-bottom:14px}
.col .img{width:340px;height:140px;margin-top:30px;border:5px solid #f0f0f0}
.col h5{font-size:15px;font-weight:700;margin-top:22px;line-height:22px}
.col p.body{font-size:15px;line-height:26px;color:#666;margin-top:10px}
.col ul{list-style:none;margin-top:10px}
.col li{font-size:15px;color:#666;line-height:34px;padding-left:22px;position:relative}
.col li:before{content:"";position:absolute;left:2px;top:13px;border-left:7px solid #999;border-top:4px solid transparent;border-bottom:4px solid transparent}
.svc{display:flex;gap:18px;margin-top:28px;align-items:flex-start}
.svc .ic{width:52px;height:52px;border-radius:50%;background:#f1f1f1;border:1px solid #ddd;flex:none;display:flex;align-items:center;justify-content:center}
.svc h6{font-size:16px;font-weight:600;color:#333}
.svc p{font-size:13px;color:#888;margin-top:4px}
/* fresh works */
.works{position:absolute;left:0;top:1375px;width:1200px;height:345px;background:var(--band)}
.works .intro{position:absolute;left:32px;top:22px;width:276px;height:300px;background:#fff;padding:26px}
.works .intro h3{font-family:"Oswald",sans-serif;font-weight:400;font-size:30px;color:#333}
.works .intro p{font-size:15px;line-height:26px;color:#666;margin-top:14px}
.works .intro .btn{left:26px;top:228px;height:40px;font-size:15px;background:#eee}
.card{position:absolute;top:22px;width:270px;height:280px;background:#fff}
.card .img{position:absolute;left:10px;top:10px;width:250px;height:210px}
.card .cap{position:absolute;left:18px;top:238px;font-size:15px;color:#555}
.card .go{position:absolute;right:16px;top:234px;width:28px;height:28px;border-radius:50%;border:1px solid #ccc;display:flex;align-items:center;justify-content:center}
.pager{position:absolute;display:flex;gap:6px}
.pager span{width:28px;height:28px;background:#fff;border:1px solid #ccc;display:flex;align-items:center;justify-content:center}
/* blog */
.sec-title{position:absolute;display:flex;align-items:center;gap:12px;font-family:"Oswald",sans-serif;font-size:30px;color:#333;border-bottom:1px solid var(--line);padding-bottom:14px}
.post{position:absolute;left:32px;width:540px;height:130px}
.post .img{position:absolute;left:0;top:0;width:210px;height:120px;border:4px solid #f0f0f0}
.post h5{position:absolute;left:242px;top:2px;font-size:15px;font-weight:700}
.post .date{position:absolute;left:242px;top:28px;font-size:12px;color:#aaa}
.post p{position:absolute;left:242px;top:52px;width:300px;font-size:15px;line-height:26px;color:#666}
.avatar{position:absolute;left:620px;top:1855px;width:130px;height:130px;border-radius:50%;background:#e7e7e7}
.quote{position:absolute;left:790px;top:1835px;width:378px;height:180px;background:#f0f0f0;padding:20px 22px}
.quote:before{content:"";position:absolute;left:-16px;top:50px;border-right:16px solid #f0f0f0;border-top:12px solid transparent;border-bottom:12px solid transparent}
.quote h5{font-size:15px;font-weight:600}
.quote p{font-size:14px;line-height:24px;color:#666;margin-top:8px}
.quote .by{font-size:12px;color:#999;margin-top:8px}
.partner{position:absolute;top:2140px;width:124px;height:96px;border:1px solid #ddd;background:#fff;display:flex;align-items:center;justify-content:center}
.partner i{display:block;width:84px;height:26px;background:#cfcfcf}
/* tweet */
.tweet{position:absolute;left:32px;top:2312px;width:1136px;height:80px;background:#4a4a4a;border-radius:8px}
.tweet .bird{position:absolute;left:14px;top:-18px;width:84px;height:84px;border-radius:50%;background:linear-gradient(#8cc4e4,#3e8fc0)}
.tweet .t1{position:absolute;left:120px;top:16px;font-size:15px;color:#ddd}
.tweet .t2{position:absolute;left:120px;top:44px;font-size:12px;color:#999}
/* footer */
.footer{position:absolute;left:0;top:2415px;width:1200px;height:365px;background:var(--dark);color:#ccc}
.footer h3{font-family:"Oswald",sans-serif;font-weight:400;font-size:38px;color:#bbb}
.footer h4{font-family:"Oswald",sans-serif;font-weight:400;font-size:30px;color:#ddd}
.fcol{position:absolute;top:20px}
.fcol li{list-style:none;font-size:15px;line-height:30px;color:#bbb}
.fcol.links li{padding-left:16px;position:relative}
.fcol.links li:before{content:"";position:absolute;left:0;top:14px;width:5px;height:5px;background:#999}
.addr{font-size:15px;line-height:24px;color:#bbb;display:flex;gap:10px;margin-top:16px}
.soc{display:flex;align-items:center;gap:12px;font-size:15px;line-height:36px;color:#bbb}
.soc i{width:22px;height:22px;border-radius:50%;background:#666;display:block}
.photos{display:grid;grid-template-columns:repeat(3,80px);gap:10px;margin-top:18px}
.photos div{width:80px;height:74px}
.bottom{position:absolute;left:0;top:2780px;width:1200px;height:62px;background:var(--darker);font-size:13px;color:#888}
</style>
</head>
<body>
<div class="page">

<header class="header">
  <div class="logo"><span class="mark"></span><span class="name">Harbor Vantage</span></div>
  <div class="contact-top"><span>hello@harborvantage-example.com</span><span>(310) 555-0148</span></div>
  <div class="search">Search
    <svg width="14" height="14" viewBox="0 0 14 14"><circle cx="6" cy="6" r="4.5" fill="none" stroke="#999" stroke-width="1.6"/><line x1="9.5" y1="9.5" x2="13" y2="13" stroke="#999" stroke-width="1.6"/></svg>
  </div>
</header>

<nav class="nav">
  <div class="home"><svg width="24" height="22" viewBox="0 0 24 22"><path d="M12 2 L2 11 H5 V20 H10 V14 H14 V20 H19 V11 H22 Z" fill="#fff"/></svg></div>
  <a>ABOUT US</a><a>FEATURES</a><a>SERVICES</a><a>PROJECTS</a><a>BLOG</a><a>CONTACT US</a><a>HOME VERSIONS</a>
</nav>

<section class="hero" role="img" aria-label="Business team in an office, smiling consultants on the phone">
  <h1><span>WELCOME TO</span> HARBOR VANTAGE</h1>
  <p>Lorem Ipsum is simply dummy text of printing and typesetting industry.</p>
  <div class="btn">know more features
    <svg width="10" height="14" viewBox="0 0 10 14"><path d="M2 1 L8 7 L2 13" fill="none" stroke="#666" stroke-width="2"/></svg></div>
</section>

<section class="strip">
  <div class="item"><div class="pic" role="img" aria-label="Smiling client portrait" style="background:#c9a98a"></div><div><h4>Smart and flexible</h4><p>simply dummy text of the typesetting industry</p></div></div>
  <div class="item"><div class="pic" role="img" aria-label="Responsive layout on devices" style="background:#8a9298"></div><div><h4>Responsive layout</h4><p>simply dummy text of the typesetting industry</p></div></div>
  <div class="item on"><div class="pic" role="img" aria-label="Businessman portrait" style="background:#9aa7b2"></div><div><h4>Easy-to-use</h4><p>simply dummy text of the typesetting industry</p></div></div>
  <div class="item"><div class="pic" role="img" aria-label="Colourful abstract swatches" style="background:linear-gradient(135deg,#e2402c,#f3c21b,#3a7cc6)"></div><div><h4>Unique colors</h4><p>simply dummy text of the typesetting industry</p></div></div>
</section>

<div class="col" style="left:32px">
  <div class="col-title"><svg width="26" height="26" viewBox="0 0 26 26"><path d="M22 13 A9 9 0 1 1 13 4" fill="none" stroke="#444" stroke-width="2.5"/><path d="M13 1 L18 4 L13 7 Z" fill="#444"/></svg>About site</div>
  <div class="img" role="img" aria-label="Hands working at a laptop" style="background:linear-gradient(#e3e6ea,#b8bfc6)"></div>
  <h5>There are many variations of passages of but the majority have alteration.</h5>
  <p class="body">Lorem Ipsum is simply dummy text of the printing and typesetting industry. Lorem Ipsum has been the industry's standard dummy text took a galley of type and scrambled it to make a type specimen book.</p>
</div>

<div class="col" style="left:422px">
  <div class="col-title"><svg width="26" height="26" viewBox="0 0 26 26"><circle cx="13" cy="14" r="10" fill="none" stroke="#444" stroke-width="2.5"/><path d="M13 8 V14 H18" fill="none" stroke="#444" stroke-width="2.5"/></svg>Why choose us</div>
  <div class="img" role="img" aria-label="Young plant growing from soil in hands" style="background:linear-gradient(#f2f2f0,#c9c2a8)"></div>
  <h5>There are many variations of passages of but the majority have alteration.</h5>
  <ul><li>Donec venenatis tibulum egestas mattis</li><li>Aenean rutrum sapien tristique dapibus</li><li>Pellentesque et vel pellentesque dictum</li><li>Maecenas et nisl nibh commodo rutrum</li></ul>
</div>

<div class="col" style="left:812px">
  <div class="col-title"><svg width="28" height="24" viewBox="0 0 28 24"><rect x="2" y="2" width="24" height="15" fill="none" stroke="#444" stroke-width="2.5"/><rect x="10" y="19" width="8" height="3" fill="#444"/></svg>Our services</div>
  <div class="svc"><div class="ic"><svg width="22" height="22"><rect x="8" y="2" width="6" height="18" fill="#d22a2a"/><rect x="2" y="8" width="18" height="6" fill="#d22a2a"/></svg></div><div><h6>Market researches</h6><p>There are many variations passages</p></div></div>
  <div class="svc"><div class="ic"><svg width="22" height="22"><circle cx="11" cy="11" r="9" fill="#3e8fc0"/></svg></div><div><h6>Management consulting</h6><p>Embarrassing hidden in the middle</p></div></div>
  <div class="svc"><div class="ic"><svg width="22" height="22"><circle cx="11" cy="11" r="9" fill="none" stroke="#d22a2a" stroke-width="3"/></svg></div><div><h6>Professional advice</h6><p>Embarrassing hidden in the middle</p></div></div>
  <div class="svc"><div class="ic"><svg width="22" height="22"><path d="M3 11 L9 17 L19 5" fill="none" stroke="#3a9a3a" stroke-width="3"/></svg></div><div><h6>Customer support</h6><p>Looked up one of the more obscure</p></div></div>
</div>

<section class="works">
  <div class="intro">
    <h3>Fresh works</h3>
    <p>Lorem Ipsum is simply dummy text of the printing and typesetting indu standard dummy text took a galley of type and specimen book.</p>
    <div class="btn">View all works <svg width="8" height="12" viewBox="0 0 8 12"><path d="M1 1 L6 6 L1 11" fill="none" stroke="#666" stroke-width="2"/></svg></div>
  </div>
  <div class="card" style="left:338px"><div class="img" role="img" aria-label="Business meeting around a table" style="background:linear-gradient(#eef0f2,#9aa4ad)"></div><span class="cap">Passages of majorite</span><span class="go"><svg width="8" height="10"><path d="M1 1 L6 5 L1 9" fill="none" stroke="#888" stroke-width="1.6"/></svg></span></div>
  <div class="card" style="left:618px"><div class="img" role="img" aria-label="Globe and financial papers" style="background:linear-gradient(#dfeaf5,#5d8fc0)"></div><span class="cap">Passages of majorite</span><span class="go"><svg width="8" height="10"><path d="M1 1 L6 5 L1 9" fill="none" stroke="#888" stroke-width="1.6"/></svg></span></div>
  <div class="card" style="left:898px"><div class="img" role="img" aria-label="Abstract dark metallic graphic" style="background:linear-gradient(135deg,#2a3c45,#6b8a96)"></div><span class="cap">Passages of majorite</span><span class="go"><svg width="8" height="10"><path d="M1 1 L6 5 L1 9" fill="none" stroke="#888" stroke-width="1.6"/></svg></span></div>
  <div class="pager" style="left:1100px;top:306px"><span><svg width="8" height="10"><path d="M6 1 L1 5 L6 9" fill="none" stroke="#888" stroke-width="1.6"/></svg></span><span><svg width="8" height="10"><path d="M1 1 L6 5 L1 9" fill="none" stroke="#888" stroke-width="1.6"/></svg></span></div>
</section>

<div class="sec-title" style="left:32px;top:1748px;width:540px"><svg width="24" height="24"><rect x="2" y="2" width="20" height="20" fill="none" stroke="#444" stroke-width="2.5"/><line x1="6" y1="9" x2="18" y2="9" stroke="#444" stroke-width="2"/><line x1="6" y1="15" x2="18" y2="15" stroke="#444" stroke-width="2"/></svg>Latest from blog/news</div>
<div class="post" style="top:1836px"><div class="img" role="img" aria-label="Colleagues reviewing documents" style="background:linear-gradient(#eceeef,#a7adb3)"></div><h5>There are variations alteration</h5><span class="date">January 18, 2013</span><p>Lorem Ipsum is simply dummy text of the printing and specimen book.</p></div>
<div class="post" style="top:1990px"><div class="img" role="img" aria-label="Team of professionals standing together" style="background:linear-gradient(#e9edf1,#8e9aa6)"></div><h5>Majority have alteration in some</h5><span class="date">January 18, 2013</span><p>Lorem Ipsum is simply dummy text of the printing and specimen book.</p></div>
<div class="post" style="top:2144px"><div class="img" role="img" aria-label="Business people in conversation" style="background:linear-gradient(#f0f0f0,#a3a3a3)"></div><h5>Consectetu from a lipsum passage</h5><span class="date">January 18, 2013</span><p>Lorem Ipsum is simply dummy text of the printing and specimen book.</p></div>

<div class="sec-title" style="left:620px;top:1748px;width:548px"><svg width="26" height="24"><path d="M3 3 H23 V16 H10 L4 21 V16 H3 Z" fill="none" stroke="#444" stroke-width="2.2"/></svg>What client say's</div>
<div class="avatar" role="img" aria-label="Client avatar"></div>
<div class="quote"><h5>There are variations alteration.</h5><p>when an unknown printer took a galley of type and scrambled it to make a type vived not only five the leap into typesetting.</p><div class="by">- Martin Ellery</div></div>

<div class="sec-title" style="left:620px;top:2058px;width:548px"><svg width="24" height="24"><circle cx="12" cy="12" r="10" fill="none" stroke="#444" stroke-width="2.2"/><ellipse cx="12" cy="12" rx="4" ry="10" fill="none" stroke="#444" stroke-width="1.6"/><line x1="2" y1="12" x2="22" y2="12" stroke="#444" stroke-width="1.6"/></svg>Customer/partners</div>
<div class="partner" style="left:620px"><i></i></div>
<div class="partner" style="left:762px"><i></i></div>
<div class="partner" style="left:904px"><i></i></div>
<div class="partner" style="left:1046px"><i></i></div>
<div class="pager" style="left:1110px;top:2246px"><span><svg width="8" height="10"><path d="M6 1 L1 5 L6 9" fill="none" stroke="#888" stroke-width="1.6"/></svg></span><span><svg width="8" height="10"><path d="M1 1 L6 5 L1 9" fill="none" stroke="#888" stroke-width="1.6"/></svg></span></div>

<div class="tweet">
  <div class="bird" role="img" aria-label="Bird mascot illustration"></div>
  <div class="t1">keelstudio Anchor Hosting - a beautiful hosting theme live on soon...</div>
  <div class="t2">yesterday · reply · retweet · favorite</div>
</div>

<footer class="footer">
  <div class="fcol" style="left:32px;width:280px">
    <h3>Harbor Vantage</h3>
    <div class="addr"><svg width="14" height="20" viewBox="0 0 14 20"><path d="M7 1 A6 6 0 0 1 13 7 C13 12 7 19 7 19 C7 19 1 12 1 7 A6 6 0 0 1 7 1 Z" fill="#bbb"/><circle cx="7" cy="7" r="2.2" fill="#3a3a3a"/></svg><div>Name of the Company<br>48 Pierline Avenue, Northgate,<br>Portview, WA 98765-0000</div></div>
    <div class="addr" style="margin-top:10px"><svg width="14" height="14"><rect x="2" y="1" width="10" height="12" rx="2" fill="#bbb"/></svg><div>1310-555-01480</div></div>
    <div class="addr" style="margin-top:4px"><svg width="14" height="14"><rect x="1" y="3" width="12" height="9" fill="#bbb"/></svg><div>0310-5550-1490</div></div>
    <div role="img" aria-label="Faint world map" style="width:200px;height:80px;margin-top:14px;background:linear-gradient(90deg,#474747,#525252,#474747);border-radius:30px"></div>
  </div>
  <div class="fcol links" style="left:330px">
    <h4>Useful links</h4>
    <ul style="margin-top:12px"><li>Our History</li><li>Professional Research</li><li>Our Development</li><li>Partnership With Us</li><li>Company Career</li><li>New Technology</li><li>Client Testimonials</li></ul>
  </div>
  <div class="fcol" style="left:622px">
    <h4>Get in touch</h4>
    <div style="margin-top:12px">
      <div class="soc"><i></i>Connect with Friendpage</div>
      <div class="soc"><i></i>Follow us on Chirpline</div>
      <div class="soc"><i></i>Sharing on Circleshare</div>
      <div class="soc"><i></i>Share videos on Clipvault</div>
      <div class="soc"><i></i>Connect with Workmesh</div>
      <div class="soc"><i></i>Subscribe rss feed</div>
    </div>
  </div>
  <div class="fcol" style="left:910px">
    <h4>Snapfeed photos</h4>
    <div class="photos">
      <div role="img" aria-label="Beach photo" style="background:linear-gradient(#6fb6e2,#e6d39a)"></div>
      <div role="img" aria-label="Palm coast photo" style="background:linear-gradient(#4aa0d8,#3d8a4a)"></div>
      <div role="img" aria-label="Island photo" style="background:linear-gradient(#7cc0e8,#2f7cae)"></div>
      <div role="img" aria-label="Coastline photo" style="background:linear-gradient(#3e8fc0,#c9b27a)"></div>
      <div role="img" aria-label="Lagoon photo" style="background:linear-gradient(#9fd3ea,#3ea0b0)"></div>
      <div role="img" aria-label="Sunset sea photo" style="background:linear-gradient(#f0b45a,#2c5f88)"></div>
    </div>
  </div>
</footer>

<div class="bottom">
  <span class="abs" style="left:32px;top:22px">Copyright © 2013 Harbor Vantage. All rights reserved.</span>
  <span class="abs" style="right:32px;top:22px">Terms of Service | Privacy Policy</span>
</div>

</div>
</body>
</html>
```